The Garden of Renewal Book Cover Contest

Book Cover Design (front, spine, and back) 6" x 9" (152.4 x 228.6 mm) book use the attached images(_4ec9c7... or Background image) on cover, or just as inspiration, or not at all.
Genre: Non-Fiction, Christian, Health, Self-Help
Book Title: The Garden of Renewal
Sub text: with Annotated Original Page Numbers, Index, and Appendix of Supporting Scientific Research.
Author: Mara J. Fenwick
Summary on back of book:
The Garden of Renewal is a timeless classic that was written over a century ago, containing life-changing principles for health and healing that continue to impact and save lives today. This book examines the life and teachings of the Master Physician (Jesus Christ) and provides practical advice.
Recent scientific advancements in the last 30 years have started to uncover some of the reasons behind why these healthful principles work. Many physicians and doctors have studied and continue to share this book, including notable names like Delia Thornbury. It is our honor to offer the "Garden of Renewal" with annotated original page numbers, index, and an appendix of supporting scientific research and additional supporting resources to help readers fully understand and apply this valuable content in their health journey and sharing with others.
I like text layered in with images (example1&2). Examples attached but use your own creativity.
Thank you for your help!
Stressed, sick, and tired women and men
Non-Fiction, Christian, Health, Self-Help

```html
<!DOCTYPE html>
<html lang="en">
<head>
<meta charset="UTF-8">
<title>The Garden of Renewal — Front Cover</title>
<link rel="stylesheet" href="https://fonts.googleapis.com/css2?family=Bebas+Neue&family=Montserrat:wght@400;500&display=swap">
<style>
  :root {
    --page-bg: #ffffff;
    --cover-yellow: #fbd56c;
    --cover-yellow-light: #fde18e;
    --title-green: #2d4a18;
    --accent-red: #cf3138;
    --band-green: #3a5a1c;
    --divider-gold: #d8a626;
    --band-text: #f4f1e6;
  }
  * { margin: 0; padding: 0; box-sizing: border-box; }
  html, body {
    width: 1200px; height: 1143px; overflow: hidden;
    background: var(--page-bg);
  }
  .cover {
    position: absolute; left: 227px; top: 12px;
    width: 746px; height: 1119px; overflow: hidden;
    background: linear-gradient(180deg, var(--cover-yellow) 0%, var(--cover-yellow) 55%, var(--cover-yellow-light) 100%);
  }
  .produce-art {
    position: absolute; left: 0; top: 0; width: 746px; height: 480px;
    background:
      radial-gradient(circle at 8% 30%, rgba(79,122,53,0.55) 0, rgba(79,122,53,0) 18%),
      radial-gradient(circle at 40% 12%, rgba(122,160,60,0.45) 0, rgba(122,160,60,0) 14%),
      radial-gradient(circle at 20% 8%, rgba(240,164,58,0.55) 0, rgba(240,164,58,0) 11%),
      radial-gradient(circle at 82% 10%, rgba(79,122,53,0.5) 0, rgba(79,122,53,0) 16%),
      radial-gradient(circle at 97% 38%, rgba(240,164,58,0.5) 0, rgba(240,164,58,0) 10%),
      radial-gradient(circle at 26% 34%, rgba(150,180,80,0.45) 0, rgba(150,180,80,0) 9%),
      linear-gradient(180deg, rgba(251,213,108,0) 70%, var(--cover-yellow) 100%);
  }
  .title {
    position: absolute; left: 0; top: 0;
    font-family: "Bebas Neue", "Oswald", sans-serif;
    font-weight: 400;
    color: var(--title-green);
    line-height: 1;
  }
  .title-line { position: absolute; white-space: nowrap; font-size: 216px; letter-spacing: -2px; }
  .title-the { left: 136px; top: 294px; }
  .title-garden { left: 118px; top: 501px; }
  .title-of { left: 118px; top: 671px; }
  .title-renewal { left: 118px; top: 839px; color: var(--accent-red); }
  .subtitle-divider {
    position: absolute; left: 278px; top: 687px;
    width: 3px; height: 153px; background: var(--divider-gold);
  }
  .subtitle {
    position: absolute; left: 301px; top: 693px; width: 370px;
    font-family: "Montserrat", sans-serif; font-weight: 500;
    font-size: 26px; line-height: 33px; color: var(--title-green);
  }
  .author-band {
    position: absolute; left: 0; bottom: 0; width: 100%; height: 72px;
    background: var(--band-green);
    display: flex; align-items: center; justify-content: center;
  }
  .author-name {
    font-family: "Montserrat", sans-serif; font-weight: 400;
    font-size: 42px; letter-spacing: 1px; color: var(--band-text);
  }
</style>
</head>
<body>
  <main class="cover">
    <div class="produce-art" role="img" aria-label="Flat-lay of fresh fruit, vegetables, leaves and grain: orange slices, kiwi halves, apples, carrots in a bowl, green leaves and wheat stalks scattered over yellow"></div>
    <h1 class="title">
      <span class="title-line title-the">THE</span>
      <span class="title-line title-garden">GARDEN</span>
      <span class="title-line title-of">OF</span>
      <span class="title-line title-renewal">RENEWAL</span>
    </h1>
    <div class="subtitle-divider"></div>
    <p class="subtitle">with Annotated Original Page Numbers, Index, and Appendix of Supporting Scientific Research.</p>
    <footer class="author-band">
      <span class="author-name">Mara J. Fenwick</span>
    </footer>
  </main>
</body>
</html>
```